Hal's Remedies Business Card Design Project

I need a business card designed for my pharmacy Hal's Remedies. I would like just the logo on one side, maybe with black background and white lettering. The other side I would also like to include my logo which is attached. Also, please include my name and the following information:
Hal Norwick Owner/Pharm D.
Business address is 7163 N Birch Rd Sioux Falls, SD 57291.
Phone number is 605-318-6027 and fax # is 605-318-6031.
my email address is hal@halsremedies.example.
My website is www.halsremedies.example.
My business hours are Monday-Friday 8am-7 pm. Saturday 8am-12 pm. Sunday Closed.
I would like the design to include my logo colors, black, white, and neon green. Silver may be added as a highlight. Thanks.
Pharmacy
See above in product description

```html
<!DOCTYPE html>
<html lang="en">
<head>
<meta charset="utf-8">
<title>Hal's Remedies – Business Card</title>
<link rel="stylesheet" href="https://fonts.googleapis.com/css2?family=Open+Sans:wght@400;600;700&display=swap">
<style>
  :root {
    --bg: #2b2b2b;
    --card-black: #1c1a1d;
    --green-light: #86c126;
    --green-dark: #5f9c18;
    --white: #ffffff;
    --soft-white: rgba(255,255,255,0.85);
    --hours-text: rgba(255,255,255,0.72);
  }
  * { box-sizing: border-box; margin: 0; padding: 0; }
  html, body {
    width: 1200px; height: 900px; overflow: hidden;
    background: var(--bg);
    font-family: "Open Sans", Verdana, sans-serif;
  }
  .canvas { position: relative; width: 1200px; height: 900px; }
  .card {
    position: absolute; left: 280px; width: 640px; height: 366px;
    border-radius: 26px; overflow: hidden;
  }
  /* Back side */
  .card-back { top: 52px; background: var(--card-black); }
  .card-back .brand {
    position: absolute; left: 0; right: 0; top: 0; bottom: 0;
    display: flex; align-items: center; justify-content: center; gap: 22px;
  }
  .brand-dot {
    width: 34px; height: 34px; border-radius: 50%; background: var(--green-light);
  }
  .card-back .brand-name {
    color: var(--white); font-weight: 600; font-size: 44px; letter-spacing: -0.5px;
  }
  /* Front side */
  .card-front {
    top: 482px;
    background: linear-gradient(160deg, var(--green-light) 0%, #7ab420 55%, var(--green-dark) 100%);
    color: var(--white);
  }
  .front-header {
    position: absolute; top: 42px; right: 46px;
    display: flex; align-items: center; gap: 14px;
  }
  .front-header .brand-dot { width: 18px; height: 18px; background: var(--white); }
  .front-header .divider { width: 1px; height: 40px; background: var(--soft-white); }
  .front-header .brand-name { font-weight: 600; font-size: 27px; letter-spacing: -0.3px; }
  .address {
    position: absolute; left: 40px; top: 50px;
    font-size: 13px; line-height: 17px; letter-spacing: 0.4px;
  }
  .person {
    position: absolute; left: 40px; top: 188px; width: 560px;
  }
  .person-row { display: flex; align-items: center; gap: 10px; }
  .person-name { font-weight: 700; font-size: 17px; white-space: nowrap; }
  .rule { flex: 1; height: 1px; background: var(--soft-white); }
  .person-title { font-size: 17px; margin-top: 1px; }
  .contacts { list-style: none; margin-top: 12px; }
  .contacts li {
    display: flex; align-items: center; gap: 8px;
    font-size: 17px; line-height: 22px;
  }
  .contacts svg { width: 14px; height: 14px; fill: var(--white); flex: none; }
  .hours {
    position: absolute; right: 60px; top: 222px;
    color: var(--hours-text); font-size: 15px; line-height: 19px;
  }
  .hours h3 { font-weight: 400; font-size: 15px; letter-spacing: 0.3px; }
  .hours table { border-collapse: collapse; }
  .hours td { padding: 0 6px 0 12px; }
  .hours td.day { padding-left: 12px; }
  .hours td.sep { padding: 0 6px 0 0; }
</style>
</head>
<body>
<main class="canvas">
  <section class="card card-back" aria-label="Card back">
    <div class="brand">
      <span class="brand-dot"></span>
      <span class="brand-name">Hal's Remedies</span>
    </div>
  </section>

  <section class="card card-front" aria-label="Card front">
    <div class="front-header">
      <span class="brand-dot"></span>
      <span class="divider"></span>
      <span class="brand-name">Hal's Remedies</span>
    </div>

    <p class="address">7163 N Birch Rd.<br>Sioux Falls, SD 57291</p>

    <div class="person">
      <div class="person-row">
        <span class="person-name">Hal Norwick</span>
        <span class="rule"></span>
      </div>
      <p class="person-title">Owner/Pharm D.</p>
      <ul class="contacts">
        <li>
          <svg viewBox="0 0 16 16" aria-hidden="true"><path d="M3.5 1.5l2.5 0 1 3.5-1.7 1.2a8 8 0 0 0 4.5 4.5l1.2-1.7 3.5 1v2.5c0 .8-.7 1.5-1.5 1.5A12 12 0 0 1 2 3c0-.8.7-1.5 1.5-1.5z"/></svg>
          605-318-6027
        </li>
        <li>
          <svg viewBox="0 0 16 16" aria-hidden="true"><rect x="4" y="1" width="8" height="4"/><rect x="1" y="6" width="14" height="6" rx="1"/><rect x="4" y="10" width="8" height="5"/></svg>
          605-318-6031
        </li>
        <li>
          <svg viewBox="0 0 16 16" aria-hidden="true"><path d="M1 3h14v10H1z M1.8 3.8L8 9l6.2-5.2" stroke="#6aa81c" stroke-width="1"/></svg>
          hal@halsremedies.example
        </li>
        <li>
          <svg viewBox="0 0 16 16" aria-hidden="true"><circle cx="8" cy="8" r="7"/><path d="M1 8h14M8 1c-3 3.5-3 10.5 0 14M8 1c3 3.5 3 10.5 0 14" stroke="#6aa81c" stroke-width="1" fill="none"/></svg>
          www.halsremedies.example
        </li>
      </ul>
    </div>

    <div class="hours">
      <h3>BUSINESS HOURS</h3>
      <table>
        <tr><td class="day">Mon–Fr</td><td class="sep">| 8am–7pm</td></tr>
        <tr><td class="day">Saturday</td><td class="sep">| 8am–12pm</td></tr>
        <tr><td class="day">Sunday</td><td class="sep">| Closed</td></tr>
      </table>
    </div>
  </section>
</main>
</body>
</html>
```